KBS PSYCHIATRIC ASSOCIATES INC NEEDS A LOGO AND BUSINESS CARD

I am changing my business name and need a fresh logo and business card. I run a psychiatric consultation service and also provide both in-person and telehealth psychiatric care.

Janet R Farrow PhD, DNP, MSN, APRN, PMHNP-BC, CNS, FNAP
8315 27th AVE CT NW
Alder Bay, OR 97410
318-555-0172

```html
<!DOCTYPE html>
<html lang="en">
<head>
<meta charset="utf-8">
<title>KBS Psychiatric Associates – Business Card</title>
<link rel="stylesheet" href="https://fonts.googleapis.com/css2?family=Marcellus&family=Alegreya+Sans:wght@700&display=swap">
<style>
  :root {
    --page: #ffffff;
    --card: #000000;
    --gold-dark: #8a5e18;
    --gold-mid: #c4963f;
    --gold-light: #fbe08a;
    --gold-solid: #c99a44;
    --gold-gradient: linear-gradient(90deg, var(--gold-dark) 0%, var(--gold-light) 30%, var(--gold-mid) 50%, var(--gold-dark) 70%, var(--gold-light) 90%, var(--gold-mid) 100%);
  }
  * { box-sizing: border-box; margin: 0; padding: 0; }
  html, body {
    width: 1077px; height: 1200px; overflow: hidden;
    background: var(--page);
  }
  .card {
    position: absolute;
    left: 249px; top: 75px;
    width: 590px; height: 1062px;
    background: var(--card);
    overflow: hidden;
  }
  .brand {
    position: absolute;
    left: 68px; top: 110px;
    width: 480px; height: 200px;
    display: flex; align-items: center; gap: 40px;
  }
  .brand-mark {
    flex: none;
    width: 118px; height: 118px;
    border-radius: 50%;
    background: var(--gold-solid);
  }
  .brand-name {
    font-family: "Alegreya Sans", sans-serif;
    font-weight: 700;
    color: var(--gold-solid);
    line-height: 1;
    width: 290px;
  }
  .brand-initials { display: block; font-size: 128px; letter-spacing: 16px; line-height: 0.95; }
  .brand-tagline { display: block; font-size: 23px; letter-spacing: 0.4px; margin-top: 6px; white-space: nowrap; }

  .gold-text {
    background: var(--gold-gradient);
    -webkit-background-clip: text; background-clip: text;
    color: transparent;
  }
  .person {
    position: absolute; left: 0; top: 443px; width: 100%;
    text-align: center;
    font-family: "Marcellus", serif;
  }
  .person-name { font-size: 64px; font-weight: 400; line-height: 1.1; }
  .person-credentials {
    margin: 18px auto 0; width: 390px;
    font-size: 22px; line-height: 25px; letter-spacing: 1px;
  }
  .divider {
    position: absolute; left: 141px; top: 670px;
    width: 309px; height: 7px;
    background: var(--gold-gradient);
  }
  .contact {
    position: absolute; left: 0; top: 750px; width: 100%;
    text-align: center;
    font-style: normal;
    font-family: "Alegreya Sans", sans-serif; font-weight: 700;
    font-size: 30px; line-height: 40.5px;
  }
  .contact span { display: block; }
  .footer-band {
    position: absolute; left: 47px; bottom: 0;
    width: 496px; height: 32px;
  }
</style>
</head>
<body>
  <main class="card">
    <header class="brand">
      <span class="brand-mark"></span>
      <span class="brand-name">
        <span class="brand-initials">KBS</span>
        <span class="brand-tagline">PSYCHIATRIC ASSOCIATES</span>
      </span>
    </header>

    <section class="person">
      <h1 class="person-name gold-text">Janet R. Farrow</h1>
      <p class="person-credentials gold-text">PhD, DNP, MSN, APRN, PMHNP-BC, CNS, FNAP</p>
    </section>

    <div class="divider"></div>

    <address class="contact gold-text">
      <span>8315 27th AVE CT NW</span>
      <span>Alder Bay, OR 97410</span>
      <span>318-555-0172</span>
    </address>

    <svg class="footer-band" viewBox="0 0 496 32" preserveAspectRatio="none" aria-hidden="true">
      <defs>
        <linearGradient id="bandGold" x1="0" y1="0" x2="1" y2="0">
          <stop offset="0" stop-color="#8a5e18"/>
          <stop offset="0.3" stop-color="#fbe08a"/>
          <stop offset="0.5" stop-color="#c4963f"/>
          <stop offset="0.7" stop-color="#8a5e18"/>
          <stop offset="0.9" stop-color="#fbe08a"/>
          <stop offset="1" stop-color="#c4963f"/>
        </linearGradient>
      </defs>
      <path d="M0 32 C25 8 50 0 80 0 L416 0 C446 0 471 8 496 32 Z" fill="url(#bandGold)"/>
    </svg>
  </main>
</body>
</html>
```